Business Card Design Project

Vexrida will provide 3D analysis of remote sensing digital data sets of airborne (aircraft/UAV) and satellite data in order to deliver 3D geospatial mapping information, videos and augmented reality products. Typical high end customers are military and security related customers, line object infrastructure owners or providers (pipelines gas/oil/fuel/water, energy lines, borders, coastal zones and rivers, transportation roads on the sea, roads, and railway systems). All these potential customers are linked to regular service monitoring, surveillance and reconnaissance covering cities, counties and countries. The company will provide 3D presentation of infrastructure (which is likely to become a binding requirement in Europe and other countries), disaster prevention and monitoring.

Target Market(s)

Target market are US based governmental agencies, such as Bureau of Civic Resilience, Federal Terrain Insight office, Ministy of Frontier Works, Bureau of Lands/Federal Terrain Registry, etc as well as commercial entities like gas, utilities, etc > Primary services will be to provide 3D geospatial mapping to support search & rescue, border control, infrastructure (pipeline, electric wires, etc.) management, agriculture, climate control, etc.

Industry/Entity Type

Business

Contact Information for Business Card

Vincent Renz6 Gristmill RdCedar Knolls, NJ 079271-973-652-8379vrenz.straight4ward@gmail.com

Requirements
Must have
• Business card must have the company logo (provided) - and want to keep with the colors in the logo

```html
<!DOCTYPE html>
<html lang="en">
<head>
<meta charset="utf-8">
<title>Vexrida — Business Card</title>
<link rel="stylesheet" href="https://fonts.googleapis.com/css2?family=Raleway:wght@300&family=Tinos&display=swap">
<style>
  :root {
    --card-bg: #ffffff;
    --brand-teal: #0f4a5e;
    --contact-ink: #1e4f6b;
    --drone-grey-light: #c9ccd0;
    --drone-grey-dark: #7d8288;
    --sat-silver: #d6d8dc;
    --sat-steel: #8f949b;
    --sat-panel: #5cc6ec;
  }
  * { margin: 0; padding: 0; box-sizing: border-box; }
  html, body { width: 1200px; height: 686px; overflow: hidden; background: var(--card-bg); }
  .card {
    position: relative;
    width: 1200px;
    height: 686px;
    background: var(--card-bg);
    overflow: hidden;
  }
  .drone-art {
    position: absolute;
    left: 21px; top: 63px;
    width: 230px; height: 80px;
    border-radius: 40px;
    background: linear-gradient(100deg, var(--drone-grey-light), var(--drone-grey-dark));
  }
  .satellite-art {
    position: absolute;
    left: 406px; top: 0;
    width: 794px; height: 389px;
    border-radius: 0 0 0 180px;
    background: linear-gradient(160deg, var(--sat-panel) 0%, var(--sat-silver) 45%, var(--sat-steel) 100%);
  }
  .brand-name {
    position: absolute;
    left: 190px; top: 168px;
    font-family: "Raleway", sans-serif;
    font-weight: 300;
    font-size: 112px;
    line-height: 1;
    color: var(--brand-teal);
    letter-spacing: 1px;
  }
  .accent-curves {
    position: absolute;
    left: 0; top: 0;
    width: 1200px; height: 686px;
  }
  .contact-icon {
    position: absolute;
    fill: var(--brand-teal);
  }
  .icon-pin { left: 394px; top: 497px; width: 36px; height: 46px; }
  .icon-mail { left: 390px; top: 598px; width: 48px; height: 40px; }
  .contact-text {
    position: absolute;
    left: 486px;
    font-family: "Tinos", "Times New Roman", serif;
    font-size: 30px;
    line-height: 38px;
    color: var(--contact-ink);
    white-space: nowrap;
  }
  .contact-address { top: 486px; }
  .contact-email { top: 599px; }
</style>
</head>
<body>
  <div class="card">
    <div class="drone-art" role="img" aria-label="Illustration of a grey surveillance drone in flight"></div>
    <div class="satellite-art" role="img" aria-label="Illustration of a silver satellite with blue solar panels"></div>

    <div class="brand-name">Vexrida</div>

    <svg class="accent-curves" viewBox="0 0 1200 686" aria-hidden="true">
      <path fill="var(--brand-teal)" d="M0,623 Q250,560 429,385 Q300,585 200,686 L0,686 Z"/>
      <path fill="var(--brand-teal)" d="M949,331 Q1150,420 1200,520 L1200,686 L1171,686 Q1110,460 949,331 Z"/>
    </svg>

    <svg class="contact-icon icon-pin" viewBox="0 0 36 46" aria-hidden="true">
      <path d="M18 0C8 0 0 8 0 18c0 12 18 28 18 28s18-16 18-28C36 8 28 0 18 0zm0 25a7 7 0 1 1 0-14 7 7 0 0 1 0 14z"/>
    </svg>
    <svg class="contact-icon icon-mail" viewBox="0 0 48 40" aria-hidden="true">
      <path d="M0 0h48v40H0z"/>
      <path d="M4 5l20 18L44 5M4 35l15-14M44 35L29 21" fill="none" stroke="#ffffff" stroke-width="2"/>
    </svg>

    <p class="contact-text contact-address">Marcus Doyle14 Larkspur LnPine Hollow,<br>NJ 070441-973-555-</p>
    <p class="contact-text contact-email">0142mdoyle.brightpath7@mailvista.example</p>
  </div>
</body>
</html>
```